Stationery for Heating Plumbing & Electrical Contractor
Veltrana
Stationery for Heating Plumbing & Electrical Contractor - Construction
Creative Brief
Professional
Neil Farrow
Director
428b Pellham Rd , Oakvane, Warrington , Cheshire QX7 3PZ
Mornwick@fenmail.com
www.veltrana.uk.com

```html
<!DOCTYPE html>
<html lang="en">
<head>
<meta charset="utf-8">
<title>Veltrana Business Cards</title>
<link href="https://fonts.googleapis.com/css2?family=Open+Sans:wght@400;600;700&display=swap" rel="stylesheet">
<style>
  :root {
    --canvas: #e9e6e1;
    --card-white: #ffffff;
    --card-dark: #3b3b3d;
    --card-dark-edge: #2a2a2c;
    --orange: #f5a623;
    --orange-deep: #e8891a;
    --ink: #4a4a4d;
    --ink-soft: #7a7a7e;
    --violet: #4b3f8f;
    --logo-grey: #8c8c90;
    --logo-light: #c9c9cc;
  }
  * { margin: 0; padding: 0; box-sizing: border-box; }
  html, body { width: 1200px; height: 978px; overflow: hidden; }
  body {
    background: var(--canvas);
    font-family: "Open Sans", Arial, sans-serif;
    position: relative;
  }
  .card {
    position: absolute;
    left: 290px;
    width: 620px;
    height: 354px;
    border-radius: 22px;
    overflow: hidden;
    box-shadow: 0 10px 28px rgba(0,0,0,0.18);
  }
  .card--back { top: 90px; background: var(--card-white); }
  .card--front {
    top: 534px;
    background: linear-gradient(135deg, #48484b 0%, var(--card-dark) 55%, var(--card-dark-edge) 100%);
  }

  /* back card */
  .back-stripe {
    position: absolute; left: 0; right: 0; bottom: 0; height: 22px;
    background: linear-gradient(90deg, var(--orange) 0%, var(--orange-deep) 30%, var(--card-dark) 34%, var(--card-dark-edge) 100%);
  }
  .back-stripe::before {
    content: ""; position: absolute; left: 0; right: 0; top: -4px; height: 4px;
    background: linear-gradient(90deg, var(--orange) 0%, rgba(245,166,35,0) 60%);
  }
  .brand {
    position: absolute; display: flex; align-items: center; gap: 12px;
  }
  .brand__dot {
    border-radius: 50%;
    background: var(--orange);
    flex: none;
  }
  .brand__name {
    font-weight: 600; color: var(--logo-grey); letter-spacing: 1px; text-transform: lowercase;
  }
  .card--back .brand { left: 40px; top: 222px; }
  .card--back .brand__dot { width: 40px; height: 40px; }
  .card--back .brand__name { font-size: 36px; }

  .contact {
    position: absolute; left: 330px; top: 44px; color: var(--ink);
  }
  .contact__name { font-size: 15px; font-weight: 700; letter-spacing: 1.5px; text-transform: uppercase; color: var(--violet); }
  .contact__role { font-size: 12px; color: var(--ink-soft); margin-top: 2px; }
  .contact__rule { width: 250px; height: 2px; background: var(--violet); margin: 12px 0 12px; }
  .contact__address { font-size: 11.5px; line-height: 1.55; color: var(--ink); margin-bottom: 12px; }
  .contact__list { list-style: none; }
  .contact__list li {
    display: flex; align-items: center; gap: 9px;
    font-size: 11.5px; line-height: 1; margin-bottom: 8px; color: var(--ink);
  }
  .contact__list svg { width: 12px; height: 12px; flex: none; }

  /* front card */
  .front-stripe {
    position: absolute; top: 0; bottom: 0; left: 46px; width: 10px;
    background: linear-gradient(180deg, var(--orange) 0%, var(--orange-deep) 100%);
  }
  .front-stripe--thin { left: 60px; width: 2px; opacity: 0.7; }
  .card--front .brand { left: 210px; top: 148px; }
  .card--front .brand__dot { width: 50px; height: 50px; }
  .card--front .brand__name { font-size: 46px; color: var(--logo-light); }
</style>
</head>
<body>
  <section class="card card--back" aria-label="Business card, contact side">
    <div class="brand">
      <span class="brand__dot"></span>
      <span class="brand__name">veltrana</span>
    </div>
    <div class="contact">
      <p class="contact__name">Neil Farrow</p>
      <p class="contact__role">Director</p>
      <div class="contact__rule"></div>
      <p class="contact__address">428b Pellham Rd , Oakvane<br>Warrington , Cheshire QX7 3PZ</p>
      <ul class="contact__list">
        <li><svg viewBox="0 0 12 12"><path d="M2 1h3l1 3-2 1a7 7 0 0 0 3 3l1-2 3 1v3c-6 0-9-3-9-9z" fill="#4a4a4d"/></svg>01925 555 0142</li>
        <li><svg viewBox="0 0 12 12"><rect x="3" y="0.5" width="6" height="11" rx="1" fill="#4a4a4d"/><rect x="4" y="2" width="4" height="7" fill="#fff"/></svg>07700 555 019</li>
        <li><svg viewBox="0 0 12 12"><rect x="1" y="4" width="10" height="6" rx="1" fill="#4a4a4d"/><rect x="3" y="1" width="6" height="4" fill="#4a4a4d"/></svg>01925 555 0143</li>
        <li><svg viewBox="0 0 12 12"><rect x="0.5" y="2" width="11" height="8" rx="1" fill="#4a4a4d"/><path d="M1 3l5 4 5-4" stroke="#fff" fill="none"/></svg>Mornwick@fenmail.com</li>
        <li><svg viewBox="0 0 12 12"><circle cx="6" cy="6" r="5.5" fill="#4b3f8f"/><path d="M0.5 6h11M6 0.5c-3 3-3 8 0 11M6 0.5c3 3 3 8 0 11" stroke="#fff" fill="none" stroke-width="0.8"/></svg>www.veltrana.uk.com</li>
      </ul>
    </div>
    <div class="back-stripe"></div>
  </section>

  <section class="card card--front" aria-label="Business card, brand side">
    <div class="front-stripe"></div>
    <div class="front-stripe front-stripe--thin"></div>
    <div class="brand">
      <span class="brand__dot"></span>
      <span class="brand__name">veltrana</span>
    </div>
  </section>
</body>
</html>
```